Meadowlark Learning Growth Partners (MLGP)

This is a professional business card. Logo and picture are a must on the front of the card. I am an educational consultant. I have been consulting for the past three years for a company. I am now opening my own company. My goal for my consulting company is to eventually consult all over America.

Target Market(s)

Educators, schools, professionals

Industry/Entity Type

Consulting

Contact Information for Business Card

Picture/logo on front, simple modern design

Font styles to use
Serif

Colors
85abd2
0355a3
3176b5
cedeed

Requirements
Must have
• picture, logo,
• Odessa Pruitt, Ed.S
• address 5073 Cormorant ridge Dr. Nashville, TN 37940
• Cell:616-555-0148
• Office: 629-555-0172
• www.Mlgpedu.example
• pruittodessa@mailbox.example

```html
<!DOCTYPE html>
<html lang="en">
<head>
<meta charset="utf-8">
<title>Meadowlark Learning Growth Partners – Business Card</title>
<link rel="stylesheet" href="https://fonts.googleapis.com/css2?family=Exo+2:wght@600&family=Arimo:wght@400;700&display=swap">
<style>
  :root {
    --page: #ffffff;
    --navy: #0a3691;
    --band-light: #85bdf0;
    --band-mid: #2f80e6;
    --line: #e6f1fc;
    --ink-brand: #0d3a8f;
    --text-light: #ffffff;
    --portrait-top: #c9b79a;
    --portrait-bottom: #1d1d24;
  }
  html, body {
    margin: 0;
    padding: 0;
    width: 1200px;
    height: 1000px;
    overflow: hidden;
    background: var(--page);
  }
  .canvas {
    position: relative;
    width: 1200px;
    height: 1000px;
  }
  .card {
    position: absolute;
    left: 74px;
    top: 199px;
    width: 1050px;
    height: 600px;
    overflow: hidden;
    background: var(--navy);
  }
  .card-waves {
    position: absolute;
    inset: 0;
  }
  .brand {
    position: absolute;
    left: 0;
    top: 0;
    width: 100%;
    height: 300px;
  }
  .brand-mark {
    position: absolute;
    left: 256px;
    top: 143px;
    width: 66px;
    height: 66px;
    border-radius: 50%;
    background: var(--ink-brand);
  }
  .brand-initials {
    position: absolute;
    left: 364px;
    top: 148px;
    margin: 0;
    font-family: "Exo 2", sans-serif;
    font-weight: 600;
    font-size: 52px;
    line-height: 56px;
    letter-spacing: 5px;
    color: var(--ink-brand);
  }
  .brand-divider {
    position: absolute;
    left: 581px;
    top: 104px;
    width: 2px;
    height: 142px;
    background: var(--ink-brand);
  }
  .brand-name {
    position: absolute;
    left: 608px;
    top: 98px;
    margin: 0;
    font-family: "Exo 2", sans-serif;
    font-weight: 600;
    font-size: 29px;
    line-height: 39px;
    letter-spacing: 1.2px;
    color: var(--ink-brand);
  }
  .portrait {
    position: absolute;
    left: 34px;
    top: 263px;
    width: 285px;
    height: 309px;
    background: linear-gradient(180deg, var(--portrait-top) 0%, #d8c0aa 45%, var(--portrait-bottom) 75%);
  }
  .contact {
    position: absolute;
    left: 341px;
    top: 388px;
    margin: 0;
    font-family: "Arimo", sans-serif;
    color: var(--text-light);
  }
  .contact-name {
    margin: 0 0 2px;
    font-weight: 700;
    font-size: 28px;
    line-height: 36px;
  }
  .contact-line {
    margin: 0;
    font-weight: 400;
    font-size: 24px;
    line-height: 31px;
  }
</style>
</head>
<body>
<main class="canvas">
  <section class="card">
    <svg class="card-waves" width="1050" height="600" viewBox="0 0 1050 600" aria-hidden="true">
      <path d="M0,52 C300,20 700,24 1050,45 L1050,300 C700,330 450,268 0,300 Z" fill="var(--band-light)"/>
      <path d="M0,52 C300,20 700,24 1050,45" fill="none" stroke="var(--line)" stroke-width="4"/>
      <path d="M0,300 C450,268 700,330 1050,300 L1050,345 C700,345 400,316 0,322 Z" fill="var(--band-mid)"/>
      <path d="M0,300 C450,268 700,330 1050,300" fill="none" stroke="#5f8fc4" stroke-width="3" opacity="0.6"/>
      <path d="M0,322 C400,316 700,345 1050,345" fill="none" stroke="var(--line)" stroke-width="4"/>
    </svg>

    <header class="brand">
      <span class="brand-mark"></span>
      <p class="brand-initials">MLGP</p>
      <span class="brand-divider"></span>
      <h1 class="brand-name">Meadowlark<br>Learning<br>Growth<br>Partners</h1>
    </header>

    <div class="portrait" role="img" aria-label="Portrait photo of Odessa Pruitt"></div>

    <address class="contact">
      <p class="contact-name">Odessa Pruitt, Ed.S</p>
      <p class="contact-line">Address: 5073 Cormorant ridge Dr. Nashville, TN 37940</p>
      <p class="contact-line">Cell: 616-555-0148</p>
      <p class="contact-line">Office: 629-555-0172</p>
      <p class="contact-line">www.Mlgpedu.example</p>
      <p class="contact-line">pruittodessa@mailbox.example</p>
    </address>
  </section>
</main>
</body>
</html>
```